business card for law firm that reflects the web site -www.MarlaQuentby.com. That is pleasant to read

We need a business card for a small law firm. Your company designed our logo - tree of life - which I can provide to the designers. The card should be on both sides. Use the coloring from the web site (www.MarlaQuentby.com) and logo (I have several formats). I am attaching the logo, but not sure what format to use.

First side name of firm: Law Office of M.K. Quentby, P.A. 4819 West Pallisor, Suite 300, Phoenix, AZ 85016, Phone: 602.555.3841, Fax: 602.555.7290, web site: www.MarlaQuentby.com, email: MQuentby@MarlaQuentby.com.
Marla K. Quentby Bankruptcy and Foreclosure Attorney & Counselor.
Back side (perhaps vertical) the logo and then Notes with lines. At the bottom: Proud to help people and small businesses file for bankruptcy protection. We are a debt relief agency.
Updates

I have several versions of the logo. Will be happy to share whatever you need. Added Sunday, April 3, 2016

Target Market(s)

everyone

Industry/Entity Type

Legal

Contact Information for Business Card

I prefer something unique (rounded edges, design that adopts my web site - www.MarlaQuentby.com.

Font styles to use
Serif

Requirements
Must have
• First side name of firm: Law Office of M.K. Quentby, P.A. 4819 West Pallisor, Suite 300, Phoenix, AZ 85016, Phone: 602.555.3841, Fax: 602.555.7290, web site: www.MarlaQuentby.com, email: MQuentby@MarlaQuentby.com.
• Marla K. Quentby Bankruptcy and Foreclosure Attorney & Counselor.
• Back side (perhaps vertical) the logo and then Notes with lines. At the bottom: Proud to help people and small businesses file for bankruptcy protection. We are a debt relief agency.
• Green and brown colors that reflect the web site: www.MarlaQuentby.com
Should not have
• Type so small that older people cannot read.

```html
<!DOCTYPE html>
<html lang="en">
<head>
<meta charset="utf-8">
<title>Law Office of M.K. Quentby, P.A. – Business Card</title>
<link rel="stylesheet" href="https://fonts.googleapis.com/css2?family=Montserrat:wght@400;500;600;700;800&family=Archivo+Black&family=Roboto+Condensed:wght@700&family=Open+Sans:wght@400&display=swap">
<style>
  :root {
    --page: #ffffff;
    --sage: #b7b89f;
    --forest: #1f3a14;
    --bark: #241612;
    --bark-line: #5a4640;
    --ruling: #6b3a46;
    --mauve: #ab92a5;
    --ink: #111111;
    --proof-blue: #0a10f5;
  }
  * { margin: 0; padding: 0; box-sizing: border-box; }
  html, body { width: 1200px; height: 1000px; overflow: hidden; background: var(--page); }
  .sheet { position: relative; width: 1200px; height: 1000px; font-family: "Montserrat", sans-serif; }

  /* ---------- Front ---------- */
  .card-front {
    position: absolute; left: 340px; top: 386px; width: 253px; height: 145px;
    border-radius: 8px; overflow: hidden; background: var(--bark);
  }
  .front-head {
    position: absolute; left: 0; top: 0; width: 100%; height: 72px;
    background: linear-gradient(to bottom, var(--sage), #ffffff);
  }
  .mark {
    position: absolute; left: 10px; top: 5px; width: 66px; height: 62px;
    display: flex; flex-direction: column; align-items: center; justify-content: center; gap: 4px;
  }
  .mark-dot { width: 34px; height: 34px; border-radius: 50%; background: var(--forest); }
  .mark-name { font-size: 9px; font-weight: 700; color: var(--forest); }
  .firm { position: absolute; left: 88px; top: 8px; width: 160px; text-align: center; color: var(--forest); }
  .firm-line1 { font-size: 15px; font-weight: 700; line-height: 18px; }
  .firm-line2 { font-size: 14px; font-weight: 500; line-height: 18px; }
  .firm-line2 small { font-size: 9px; }
  .attorney { position: absolute; right: 5px; top: 50px; text-align: right; color: var(--forest); }
  .attorney-name { font-size: 10px; font-weight: 500; line-height: 11px; }
  .attorney-role { font-size: 6.5px; font-weight: 700; line-height: 9px; }
  .dash { position: absolute; left: 4px; right: 4px; border-top: 1px dashed var(--bark-line); }
  .dash.top { top: 76px; } .dash.bottom { top: 139px; }
  .web { position: absolute; left: 16px; top: 88px; width: 116px; text-align: center; color: #fff; font-size: 8px; font-weight: 700; line-height: 12px; }
  .phones { position: absolute; right: 8px; top: 78px; width: 80px; text-align: center; color: #fff; }
  .phones span { display: block; font-size: 7.5px; line-height: 9px; }
  .phones strong { display: block; font-size: 12px; font-weight: 700; line-height: 13px; margin-bottom: 1px; }
  .address { position: absolute; left: 0; top: 126px; width: 100%; text-align: center; color: #fff; font-size: 7.4px; }

  /* ---------- Back ---------- */
  .card-back {
    position: absolute; left: 667px; top: 288px; width: 144px; height: 252px;
    border-radius: 8px; overflow: hidden;
    background: linear-gradient(to bottom, var(--sage) 0%, #ffffff 42%, #e6dce3 65%, var(--mauve) 100%);
  }
  .back-mark {
    position: absolute; left: 28px; top: 7px; width: 88px; height: 88px;
    display: flex; flex-direction: column; align-items: center; justify-content: center; gap: 6px;
  }
  .back-mark .mark-dot { width: 52px; height: 52px; }
  .back-mark .mark-name { font-size: 11px; }
  .notes-label { position: absolute; left: 0; top: 99px; width: 100%; text-align: center; font-size: 7px; font-weight: 700; color: var(--ink); }
  .notes-label span { border-bottom: 1px solid var(--ruling); padding: 0 3px; }
  .ruling { position: absolute; left: 13px; top: 117px; }
  .pledge { position: absolute; left: 0; top: 227px; width: 100%; text-align: center; font-size: 5.2px; font-weight: 700; line-height: 6px; color: var(--ink); }

  /* ---------- Proof footer ---------- */
  .proof-word { position: absolute; left: 12px; top: 832px; font-family: "Archivo Black", sans-serif; font-size: 31px; color: #000; letter-spacing: 1px; }
  .proof-bar { position: absolute; left: 148px; top: 837px; width: 1042px; height: 26px; background: var(--proof-blue); }
  .label { position: absolute; font-family: "Roboto Condensed", sans-serif; font-weight: 700; font-size: 13px; color: #000; }
  .prepared-label { left: 249px; top: 880px; }
  .notes-field { left: 730px; top: 880px; }
  .client { position: absolute; left: 289px; top: 935px; font-family: "Open Sans", sans-serif; font-size: 19px; color: #000; }
</style>
</head>
<body>
<main class="sheet">

  <section class="card-front" aria-label="Business card front">
    <div class="front-head"></div>
    <div class="mark"><div class="mark-dot"></div><div class="mark-name">Quentby</div></div>
    <div class="firm">
      <div class="firm-line1">Law Office of</div>
      <div class="firm-line2">M.K. Quentby, <small>P.A.</small></div>
    </div>
    <div class="attorney">
      <div class="attorney-name">Marla K. Quentby</div>
      <div class="attorney-role">Bankruptcy and Foreclosure Attorney &amp; Counselor</div>
    </div>
    <div class="dash top"></div>
    <div class="web">www.MarlaQuentby.com<br>MQuentby@MarlaQuentby.com</div>
    <div class="phones">
      <span>Phone</span><strong>602.555.3841</strong>
      <span>Fax</span><strong>602.555.7290</strong>
    </div>
    <div class="address">4819 West Pallisor, Suite 300, Phoenix, AZ 85016</div>
    <div class="dash bottom"></div>
  </section>

  <section class="card-back" aria-label="Business card back">
    <div class="back-mark"><div class="mark-dot"></div><div class="mark-name">Quentby</div></div>
    <div class="notes-label"><span>NOTES</span></div>
    <svg class="ruling" width="118" height="106" viewBox="0 0 118 106" aria-hidden="true">
      <g stroke="#6b3a46" stroke-width="0.8">
        <line x1="0" y1="1" x2="118" y2="1"/><line x1="0" y1="14" x2="118" y2="14"/>
        <line x1="0" y1="27" x2="118" y2="27"/><line x1="0" y1="40" x2="118" y2="40"/>
        <line x1="0" y1="53" x2="118" y2="53"/><line x1="0" y1="66" x2="118" y2="66"/>
        <line x1="0" y1="79" x2="118" y2="79"/><line x1="0" y1="92" x2="118" y2="92"/>
        <line x1="0" y1="105" x2="118" y2="105"/>
      </g>
    </svg>
    <p class="pledge">Proud to help people and small businesses<br>file for bankruptcy protection.<br>We are a debt relief agency.</p>
  </section>

  <div class="proof-word">PROOF</div>
  <div class="proof-bar"></div>
  <div class="label prepared-label">PREPARED FOR:</div>
  <div class="label notes-field">NOTES:</div>
  <div class="client">Marla K Quentby</div>

</main>
</body>
</html>
```